lantern pathway for children needs a website designer

We need a website designer for our new extension to our company known as 'lantern pathway' providing shadow support services to children based in Singapore. We are a sister branch of a private clinic 'Bright horizon' providing speech language, occupational, and educational therapy to children.

We would like to use our own photos. So the selected design should have a frame with pictures to give us an idea but we will replace them with our own. We will be needing help with inputting information and changing information throughout.

We would like to see designs that are simple, and professional. We have a logo (see attached). The result should convey professionalism in shadow support, fostering independent thinking and moving students towards self-learning.

Target Market(s)

Teachers, psychologists, parents

Industry/Entity Type

Clinic

Requirements
Should not have
• too distracting colours

```html
<!DOCTYPE html>
<html lang="en">
<head>
<meta charset="utf-8">
<title>Lantern Pathway – Shadow Support</title>
<link href="https://fonts.googleapis.com/css2?family=Source+Sans+3:wght@400;600;700&family=PT+Sans:wght@700&display=swap" rel="stylesheet">
<style>
:root{
  --maroon:#7a1c26;
  --maroon-dark:#5e1119;
  --maroon-light:#8c2a33;
  --ink:#333;
  --muted:#777;
  --line:#dcdcdc;
  --yellow:#f5ea14;
}
*{box-sizing:border-box;margin:0;padding:0}
html,body{width:947px;height:1200px;overflow:hidden}
body{position:relative;background:linear-gradient(#dedede 0,#d6d6d6 395px,#f1f1f1 395px,#f1f1f1 100%);font-family:"Source Sans 3",sans-serif;color:var(--ink)}
.abs{position:absolute}
.topbar{left:0;top:0;width:947px;height:28px;background:linear-gradient(var(--maroon-light),var(--maroon-dark))}
.topbar nav{position:absolute;left:79px;top:7px;font-size:11px;color:#fff}
.topbar nav span{margin-right:14px}
.topbar .dots{position:absolute;right:79px;top:8px;display:flex;gap:9px}
.topbar .dots i{display:block;width:11px;height:11px;border-radius:2px;background:#c9c9c9}
.brand{left:99px;top:60px;display:flex;align-items:center;gap:10px}
.brand .mark{width:34px;height:34px;border-radius:50%;background:var(--maroon)}
.brand .name{font-size:31px;font-weight:700;color:var(--maroon)}
.contact{left:638px;font-size:14px;color:var(--maroon);display:flex;align-items:center;gap:14px}
.contact .ico{width:32px;height:32px;border-radius:50%;background:var(--maroon);display:flex;align-items:center;justify-content:center}
.contact.phone{top:48px}
.contact.mail{top:91px;font-size:11px;gap:12px}
.page{left:77px;top:137px;width:791px;height:1063px;background:#fff;border-top:6px solid var(--maroon)}
.mainnav{left:77px;top:143px;width:791px;height:52px;background:#f4f4f4;display:flex;font-size:11px;color:var(--muted)}
.mainnav a{display:flex;align-items:center;justify-content:center;border-right:1px solid var(--line);height:100%}
.mainnav .search{width:148px;height:21px;border:1px solid #ccc;background:#fff;margin:16px 0 0 0}
.hero{left:77px;top:195px;width:790px;height:312px;background:linear-gradient(120deg,#3e5a78 0%,#b8c6d4 30%,#e8eef2 55%,#c9d2d9 80%,#9aa7b3 100%)}
.caption{left:133px;top:321px;width:383px;height:145px;background:rgba(40,40,40,.82)}
.caption h1{position:absolute;left:16px;top:8px;font-family:"PT Sans",sans-serif;font-size:29px;color:var(--yellow);white-space:nowrap}
.caption ul{position:absolute;left:65px;top:56px;list-style:none;font-size:10.5px;color:#fff}
.caption li{height:30px;white-space:nowrap}
.caption li::before{content:"››";font-weight:700;margin:0 10px 0 -16px}
.arrow{top:457px;width:33px;height:33px;border-radius:50%;background:#333;display:flex;align-items:center;justify-content:center}
.card{width:235px}
.card h2{display:flex;align-items:center;gap:11px;font-size:19px;font-weight:400;color:var(--maroon);height:36px}
.card h2 .ic{width:37px;height:37px;border-radius:50%;background:var(--maroon);flex:none;display:flex;align-items:center;justify-content:center}
.card p{margin:10px 0 0 4px;font-size:11px;line-height:20px;text-align:justify;height:60px;overflow:hidden}
.vdiv{width:1px;height:108px;background:var(--line);top:543px}
.hdiv{height:1px;width:235px;background:var(--line);top:671px}
.band{left:76px;top:828px;width:790px;height:274px;background:linear-gradient(var(--maroon-light),var(--maroon-dark));color:#fff}
.band h2{position:absolute;top:11px;width:100%;text-align:center;font-size:20px;font-weight:700}
.item{position:absolute;top:74px;width:232px;text-align:center}
.item .circle{width:68px;height:68px;border-radius:50%;background:#fff;margin:0 auto;display:flex;align-items:center;justify-content:center}
.item h3{font-size:15px;font-weight:400;margin-top:14px;line-height:20px;height:44px}
.item p{font-size:9.5px;line-height:20px;text-align:justify;margin-top:8px}
.footer{left:77px;top:1139px;width:791px;border-top:1px solid var(--line)}
.footer nav{position:absolute;left:18px;top:13px;font-size:11px;color:#888;white-space:nowrap;word-spacing:1px}
.footer small{position:absolute;left:18px;top:33px;font-size:8.5px;color:#999;white-space:nowrap}
.social{left:730px;top:1153px;display:flex;gap:2px}
.social i{width:29px;height:29px;border-radius:50%;background:#9a9a9a;display:block}
</style>
</head>
<body>
<div class="abs topbar">
  <nav><span>Home</span><span>About</span><span>siteMap</span><span>Contact</span></nav>
  <div class="dots"><i></i><i></i><i></i><i></i><i></i><i></i></div>
</div>

<div class="abs brand"><span class="mark"></span><span class="name">Lantern Pathway</span></div>

<div class="abs contact phone">
  <span class="ico"><svg width="15" height="15" viewBox="0 0 24 24"><path fill="#fff" d="M6.6 10.8a15 15 0 0 0 6.6 6.6l2.2-2.2c.3-.3.7-.4 1-.2 1.1.4 2.3.6 3.6.6.6 0 1 .4 1 1V20c0 .6-.4 1-1 1A17 17 0 0 1 3 4c0-.6.4-1 1-1h3.5c.6 0 1 .4 1 1 0 1.3.2 2.5.6 3.6.1.3 0 .7-.2 1z"/></svg></span>
  <span>Call us : + 65 6100 2480</span>
</div>
<div class="abs contact mail">
  <span class="ico"><svg width="16" height="14" viewBox="0 0 24 20"><path fill="none" stroke="#fff" stroke-width="2" d="M2 2h20v16H2z M2 2l10 8 10-8"/></svg></span>
  <span>enquiries@quillbrook-therapy.sg</span>
</div>

<div class="abs page"></div>

<nav class="abs mainnav">
  <a style="width:61px">Home</a><a style="width:74px">About Us</a><a style="width:82px">Mission</a><a style="width:92px">Our Services</a><a style="width:115px">Shadow Support</a><a style="width:106px">For Referrers</a><a style="width:83px;border:0">Contact us</a>
  <span class="search"></span>
  <svg style="margin:18px 0 0 6px" width="14" height="14" viewBox="0 0 14 14"><circle cx="5.5" cy="5.5" r="4.3" fill="none" stroke="#888" stroke-width="1.6"/><path d="M8.7 8.7l4 4" stroke="#888" stroke-width="1.8"/></svg>
</nav>

<div class="abs hero" role="img" aria-label="Photo of clinicians in white coats reviewing work together at a computer"></div>
<div class="abs caption">
  <h1>Lantern Pathway aims to</h1>
  <ul><li>work in an integrated manner,</li><li>respecting the work of the respective</li><li>professionals involved and collaborating effectively.</li></ul>
</div>
<div class="abs arrow" style="left:777px"><svg width="12" height="16"><path d="M9 2L3 8l6 6" stroke="#fff" stroke-width="2.5" fill="none"/></svg></div>
<div class="abs arrow" style="left:812px"><svg width="12" height="16"><path d="M3 2l6 6-6 6" stroke="#fff" stroke-width="2.5" fill="none"/></svg></div>

<section class="abs card" style="left:89px;top:545px"><h2><span class="ic"><svg width="16" height="16"><circle cx="8" cy="5" r="4" fill="#fff"/><rect x="1" y="10" width="14" height="6" rx="3" fill="#fff"/></svg></span>About Us</h2>
<p>Lantern Pathway is part of the Quillbrook Therapy Group of Companies, who are providing speech language therapy, occupational and educational therapy.</p></section>
<section class="abs card" style="left:361px;top:545px"><h2><span class="ic"><svg width="14" height="14"><rect x="1" y="3" width="12" height="10" fill="#fff"/><path d="M7 5v6M4 8h6" stroke="#7a1c26" stroke-width="1.5"/></svg></span>Mission</h2>
<p>Lantern Pathway was borne out of our Speech language Pathologists’ frustration at a frequent lack of carry-over of goals to a student’s classroom setting.</p></section>
<section class="abs card" style="left:624px;top:545px"><h2><span class="ic"><svg width="14" height="14"><rect x="2" y="2" width="10" height="11" fill="none" stroke="#fff" stroke-width="1.5"/><path d="M4 6h6M4 9h6" stroke="#fff"/></svg></span>Our Services</h2>
<p>• Train shadows with a strong focus on equipping them with dynamic, clinical skills.<br>• Provide families with well-trained Shadows</p></section>

<div class="abs vdiv" style="left:339px"></div>
<div class="abs vdiv" style="left:603px"></div>
<div class="abs hdiv" style="left:89px"></div>
<div class="abs hdiv" style="left:361px"></div>
<div class="abs hdiv" style="left:622px"></div>
<div class="abs vdiv" style="left:339px;top:683px"></div>
<div class="abs vdiv" style="left:603px;top:683px"></div>

<section class="abs card" style="left:89px;top:685px"><h2><span class="ic"><svg width="14" height="16"><rect x="2" y="3" width="10" height="12" fill="none" stroke="#fff" stroke-width="1.5"/><rect x="5" y="1" width="4" height="3" fill="#fff"/></svg></span>Register As A Shadow</h2>
<p>A shadow support is para-professional who can help a struggling student to integrate and learn in their school environment. At different points</p></section>
<section class="abs card" style="left:361px;top:685px"><h2><span class="ic"><svg width="14" height="14"><rect x="1" y="1" width="12" height="9" fill="none" stroke="#fff" stroke-width="1.5"/><path d="M4 13h6M7 10v3" stroke="#fff" stroke-width="1.5"/></svg></span>For Referrers</h2>
<p>• Shadow Support will participate in a collaborative working relationship with the professionals working with each student to support goals.</p></section>
<section class="abs card" style="left:624px;top:685px"><h2><span class="ic"><svg width="16" height="16"><circle cx="10" cy="3" r="2" fill="#fff"/><path d="M4 6l5-1 2 4 3 1M9 5l-2 5 3 2-1 3M7 10l-4 3" stroke="#fff" stroke-width="1.6" fill="none"/></svg></span>We Help You Achieve</h2>
<p>• Shadows support the academic/behavioral goals set out on the Individualised Education Plan</p></section>

<section class="abs band">
  <h2>Shadow Support</h2>
  <div class="item" style="left:10px">
    <div class="circle"><svg width="30" height="40"><circle cx="8" cy="6" r="3.5" fill="#7a1c26"/><circle cx="22" cy="6" r="3.5" fill="#7a1c26"/><path d="M5 11h6l1 14H4zM19 11h6l2 14h-10z" fill="#7a1c26"/><path d="M6 25v12M10 25v12M20 25v12M24 25v12" stroke="#7a1c26" stroke-width="2.5"/></svg></div>
    <h3>What is shadow support?</h3>
    <p>A shadow support is para-professional who can help a struggling student to integrate and learn in their school environment. At different points in a student’s life,</p>
  </div>
  <div class="item" style="left:282px">
    <div class="circle"><svg width="30" height="30"><circle cx="8" cy="8" r="6" fill="none" stroke="#7a1c26" stroke-width="2"/><rect x="10" y="12" width="18" height="16" fill="none" stroke="#7a1c26" stroke-width="2"/><path d="M14 16h3M21 16h3M14 21h3M21 21h3" stroke="#7a1c26" stroke-width="2"/></svg></div>
    <h3>What are its Advantages?</h3>
    <p>A shadow support is para-professional who can help a struggling student to integrate and learn in their school environment. At different points in a student’s life,</p>
  </div>
  <div class="item" style="left:547px">
    <div class="circle" style="transform:translateX(-19px)"><svg width="36" height="46"><circle cx="24" cy="5" r="4" fill="#7a1c26"/><path d="M19 11h10v16h-2v17h-6V27h-2z" fill="#7a1c26"/><circle cx="9" cy="22" r="3" fill="#7a1c26"/><path d="M5 27h8v8h-2v9H7v-9H5z" fill="#7a1c26"/><path d="M12 28l7-4" stroke="#7a1c26" stroke-width="2"/></svg></div>
    <h3 style="transform:translateX(-5px)">How do I know if my child<br>needs shadowing</h3>
    <p>A shadow support is para-professional who can help a struggling student to integrate and learn in their school environment. At different points in a student’s life,</p>
  </div>
</section>

<footer class="abs footer">
  <nav>Home &nbsp;&nbsp;|&nbsp;&nbsp; About Us &nbsp;&nbsp;|&nbsp;&nbsp; Mission &nbsp;|&nbsp; Our Services &nbsp;&nbsp;|&nbsp;&nbsp; Shadow Support &nbsp;&nbsp;|&nbsp;&nbsp; For Referrers &nbsp;&nbsp;&nbsp;|&nbsp; Contact us</nav>
  <small>© 2014 Company Name. All right reserved. Term of Use</small>
</footer>
<div class="abs social"><i></i><i></i><i></i><i></i></div>
</body>
</html>
```